Business Card Design Project

We are looking for a new business card design for a Drilling company in WA, Australia.

We are in between offices, however require a design in the meantime due to some upcoming events with our basic information.

The Logo for our company is Blue and Grey and would like this colour scheme throughout.

We are quite a new company so would like a memorable design that stands out and communicates a strong commitment to safety, quality of work and performance.

The company name is Ironbark Boring Group (IBG)

The details to be included are as follows:

Gavin Thorley
Managing Director
m.0481639207
e.gavin@ibgpty.com.au

Martin Thorley
Director
m.0419852637
e.martin@ibgpty.com.au

Industry/Entity Type

Events

Requirements
Must have
• Under the Logo, we would like 'Western Australia'

```html
<!DOCTYPE html>
<html lang="en">
<head>
<meta charset="utf-8">
<title>Ironbark Boring Group – Business Cards</title>
<link rel="stylesheet" href="https://fonts.googleapis.com/css2?family=PT+Sans+Narrow:wght@400;700&display=swap">
<style>
  :root {
    --stage: #1c1c1c;
    --paper: #ffffff;
    --paper-shade: #e6e6e6;
    --navy: #223a85;
    --navy-deep: #1a2a78;
    --navy-dark: #141f5c;
    --grey: #7a7a7a;
    --text-light: #ffffff;
    --divider: rgba(255,255,255,0.35);
  }
  * { box-sizing: border-box; margin: 0; padding: 0; }
  html, body {
    width: 1200px; height: 900px; overflow: hidden;
    background: var(--stage);
    font-family: "PT Sans Narrow", "Arial Narrow", sans-serif;
  }
  .card-sheet {
    position: relative; width: 1200px; height: 900px;
  }
  .card {
    position: absolute; top: 325px;
    width: 450px; height: 250px;
    background: var(--paper);
    overflow: hidden;
  }
  .card--front {
    left: 128px;
    background: linear-gradient(180deg, var(--paper-shade) 0%, var(--paper) 55%);
    display: flex; flex-direction: column; align-items: center; justify-content: center;
  }
  .card--back { left: 622px; }

  .wordmark {
    display: flex; align-items: center; gap: 8px;
  }
  .wordmark__mark {
    width: 14px; height: 14px; background: var(--navy);
  }
  .wordmark__name {
    font-weight: 700; color: var(--navy);
    font-size: 25px; letter-spacing: 0.2px; line-height: 1;
  }
  .region {
    margin-top: 8px;
    font-weight: 700; color: var(--grey);
    font-size: 18px; line-height: 1;
  }

  .back__header {
    height: 93px;
    display: flex; align-items: center; justify-content: center;
    background: var(--paper);
  }
  .back__band {
    position: relative; height: 157px;
    background:
      radial-gradient(ellipse at 20% 30%, rgba(70,90,170,0.35), transparent 60%),
      linear-gradient(160deg, var(--navy-deep) 0%, var(--navy) 50%, var(--navy-dark) 100%);
    display: flex;
  }
  .back__band::before {
    content: ""; position: absolute;
    left: 50%; top: 12px; height: 66px; width: 1px;
    background: var(--divider);
  }
  .contact {
    flex: 1; color: var(--text-light); text-align: center;
    padding-top: 26px;
  }
  .contact__name { font-weight: 700; font-size: 20px; line-height: 1.1; }
  .contact__role { font-size: 12px; margin-top: 3px; }
  .contact__details { font-size: 11px; margin-top: 38px; line-height: 1.35; }
</style>
</head>
<body>
<main class="card-sheet">
  <section class="card card--front" aria-label="Card front">
    <div class="wordmark">
      <span class="wordmark__mark"></span>
      <span class="wordmark__name">Ironbark Boring Group</span>
    </div>
    <p class="region">Western Australia</p>
  </section>

  <section class="card card--back" aria-label="Card back">
    <header class="back__header">
      <div class="wordmark">
        <span class="wordmark__mark"></span>
        <span class="wordmark__name">Ironbark Boring Group</span>
      </div>
    </header>
    <div class="back__band">
      <div class="contact">
        <p class="contact__name">Gavin Thorley</p>
        <p class="contact__role">Managing Director</p>
        <p class="contact__details">m.0481639207<br>e.gavin@ibgpty.com.au</p>
      </div>
      <div class="contact">
        <p class="contact__name">Martin Thorley</p>
        <p class="contact__role">Director</p>
        <p class="contact__details">m.0419852637<br>e.martin@ibgpty.com.au</p>
      </div>
    </div>
  </section>
</main>
</body>
</html>
```